Business card for Autism Consultancy

I need a double-sided business card for Brightpath Learning Consultancy
Please try to use the colours and graphics in line with our website www.brightpathlearn.nz
Front side
Logo and the name of the company – Brightpath Learning Consultancy
We use Child-Centred, Modern and Innovative approaches
Teaching autistic children to bond, laugh and play
www.brightpathlearn.nz
info@brightpathlearn.nz
phone +64 09 37 615 48
Back side
Photo
Mirela Dunstan
Founder
Postgraduate Autism (Children) Specialist (with Merit)
Qualified by the Faculty of Learning Support and Access Studies (FLSA), Harwell Vale University
mirela@brightpathlearn.nz
phone +64 937 615 48
mobile: +64 20 6283 9150
Please do not convert the text fields to outlines, i.e. I need to be able to edit any text after.
The final design should be either in Adobe Illustrator or Adobe Photoshop format.
The Specs for the business card are:
Full Bleed Size
94 x 58 mm
1110 x 685 pixels
Document Trim Size
91 x 55 mm
1075 x 650 pixels

```html
<!DOCTYPE html>
<html lang="en">
<head>
<meta charset="utf-8">
<title>Brightpath Learning Consultancy – Business Card</title>
<link rel="stylesheet" href="https://fonts.googleapis.com/css2?family=Fira+Sans+Condensed:wght@400;500;700&display=swap">
<style>
  :root {
    --navy: #1f2d5c;
    --navy-deep: #1a2650;
    --yellow: #fdd22a;
    --teal: #3cc1b4;
    --grey: #8a8d93;
    --paper: #ffffff;
    --backdrop: #e6e7ea;
    --ink: #1f2d5c;
  }
  * { box-sizing: border-box; margin: 0; padding: 0; }
  html, body { width: 857px; height: 1200px; overflow: hidden; }
  body {
    background: var(--backdrop);
    font-family: "Fira Sans Condensed", sans-serif;
    position: relative;
  }
  .card {
    position: absolute;
    left: 86px;
    width: 691px;
    height: 427px;
    background: var(--paper);
    overflow: hidden;
  }
  .card--front { top: 90px; }
  .card--back { top: 621px; }
  .card__waves { position: absolute; inset: 0; width: 691px; height: 427px; }

  /* Front */
  .front__intro {
    position: absolute; top: 30px; left: 0; width: 100%;
    text-align: center; font-size: 21px; color: var(--ink);
  }
  .front__intro strong { color: var(--teal); font-weight: 500; }
  .brand {
    position: absolute; top: 92px; left: 138px;
    display: flex; align-items: center; gap: 22px;
  }
  .brand__dot {
    width: 110px; height: 110px; border-radius: 50%;
    background: var(--yellow); flex: none;
  }
  .brand__name {
    font-size: 38px; font-weight: 700; line-height: 1.1;
    color: var(--navy); width: 300px;
  }
  .front__mission {
    position: absolute; top: 294px; left: 0; width: 100%;
    text-align: center; font-size: 21px; color: var(--navy);
  }
  .front__mission strong { font-weight: 700; }
  .contacts {
    position: absolute; left: 0; width: 100%;
    display: flex; justify-content: center; align-items: center; gap: 14px;
    font-size: 17px; color: #fff;
  }
  .front__contacts { top: 372px; }
  .contact { display: flex; align-items: center; gap: 8px; }
  .contact svg { width: 14px; height: 14px; flex: none; }

  /* Back */
  .portrait {
    position: absolute; left: 262px; top: 32px;
    width: 167px; height: 167px; border-radius: 50%;
    background: #fff; border: 3px solid #dcdde0;
    display: flex; align-items: center; justify-content: center;
  }
  .portrait__photo {
    width: 151px; height: 151px; border-radius: 50%;
    background: radial-gradient(circle at 50% 40%, #d9a98e 0%, #8a5a43 55%, #3a2a24 100%);
  }
  .person { position: absolute; top: 213px; left: 0; width: 100%; text-align: center; color: #fff; }
  .person__name { font-size: 24px; font-weight: 700; color: var(--yellow); letter-spacing: 0.2px; }
  .person__role { font-size: 16px; margin-top: 6px; }
  .person__specialism { font-size: 16px; color: var(--teal); margin-top: 9px; }
  .person__qualification { font-size: 16px; margin-top: 9px; line-height: 1.4; }
  .back__contacts { top: 374px; gap: 16px; }
</style>
</head>
<body>

<section class="card card--front" aria-label="Business card front">
  <svg class="card__waves" viewBox="0 0 691 427" aria-hidden="true">
    <path fill="var(--yellow)" d="M0,272 q13.3,-14 26.6,0 t26.6,0 t26.6,0 t26.6,0 t26.6,0 t26.6,0 t26.6,0 t26.6,0 t26.6,0 t26.6,0 t26.6,0 t26.6,0 t26.6,0 t26.6,0 t26.6,0 t26.6,0 t26.6,0 t26.6,0 t26.6,0 t26.6,0 t26.6,0 t26.6,0 t26.6,0 t26.6,0 t26.6,0 t26.6,0 L691,427 L0,427 Z"/>
    <path fill="var(--navy)" d="M0,350 q13.3,-14 26.6,0 t26.6,0 t26.6,0 t26.6,0 t26.6,0 t26.6,0 t26.6,0 t26.6,0 t26.6,0 t26.6,0 t26.6,0 t26.6,0 t26.6,0 t26.6,0 t26.6,0 t26.6,0 t26.6,0 t26.6,0 t26.6,0 t26.6,0 t26.6,0 t26.6,0 t26.6,0 t26.6,0 t26.6,0 t26.6,0 L691,427 L0,427 Z"/>
  </svg>

  <p class="front__intro">We use child-centred, <strong>Modern &amp; Innovative</strong> approaches</p>

  <div class="brand">
    <span class="brand__dot"></span>
    <span class="brand__name">Brightpath Learning Consultancy</span>
  </div>

  <p class="front__mission">Teaching autistic children to <strong>BOND, LAUGH AND PLAY</strong></p>

  <div class="contacts front__contacts">
    <span class="contact">
      <svg viewBox="0 0 14 14" aria-hidden="true"><circle cx="7" cy="7" r="7" fill="var(--yellow)"/><path d="M4.3,3.6 l1.4,-0.4 0.7,1.8 -0.8,0.6 q0.6,1.5 2,2.3 l0.7,-0.7 1.7,0.8 -0.4,1.4 q-3.8,0.2 -5.3,-5.8z" fill="var(--navy)"/></svg>
      +64 09 37 615 48
    </span>
    <span class="contact">
      <svg viewBox="0 0 14 14" aria-hidden="true"><circle cx="7" cy="7" r="7" fill="var(--yellow)"/><rect x="3.5" y="4.5" width="7" height="5" rx="0.6" fill="var(--navy)"/><path d="M3.8,4.9 L7,7.3 10.2,4.9" stroke="var(--yellow)" stroke-width="0.8" fill="none"/></svg>
      info@brightpathlearn.nz
    </span>
    <span class="contact">
      <svg viewBox="0 0 14 14" aria-hidden="true"><circle cx="7" cy="7" r="7" fill="var(--yellow)"/><g stroke="var(--navy)" stroke-width="0.8" fill="none"><circle cx="7" cy="7" r="3.6"/><ellipse cx="7" cy="7" rx="1.5" ry="3.6"/><path d="M3.4,7 H10.6"/></g></svg>
      www.brightpathlearn.nz
    </span>
  </div>
</section>

<section class="card card--back" aria-label="Business card back">
  <svg class="card__waves" viewBox="0 0 691 427" aria-hidden="true">
    <path fill="var(--yellow)" d="M0,98 q13.3,-14 26.6,0 t26.6,0 t26.6,0 t26.6,0 t26.6,0 t26.6,0 t26.6,0 t26.6,0 t26.6,0 t26.6,0 t26.6,0 t26.6,0 t26.6,0 t26.6,0 t26.6,0 t26.6,0 t26.6,0 t26.6,0 t26.6,0 t26.6,0 t26.6,0 t26.6,0 t26.6,0 t26.6,0 t26.6,0 t26.6,0 L691,427 L0,427 Z"/>
    <path fill="#ffffff" d="M0,110 q13.3,14 26.6,0 t26.6,0 t26.6,0 t26.6,0 t26.6,0 t26.6,0 t26.6,0 t26.6,0 t26.6,0 t26.6,0 t26.6,0 t26.6,0 t26.6,0 t26.6,0 t26.6,0 t26.6,0 t26.6,0 t26.6,0 t26.6,0 t26.6,0 t26.6,0 t26.6,0 t26.6,0 t26.6,0 t26.6,0 t26.6,0 L691,427 L0,427 Z"/>
    <path fill="var(--navy)" d="M0,116 q13.3,14 26.6,0 t26.6,0 t26.6,0 t26.6,0 t26.6,0 t26.6,0 t26.6,0 t26.6,0 t26.6,0 t26.6,0 t26.6,0 t26.6,0 t26.6,0 t26.6,0 t26.6,0 t26.6,0 t26.6,0 t26.6,0 t26.6,0 t26.6,0 t26.6,0 t26.6,0 t26.6,0 t26.6,0 t26.6,0 t26.6,0 L691,427 L0,427 Z"/>
  </svg>

  <div class="portrait">
    <div class="portrait__photo" role="img" aria-label="Portrait photo of Mirela Dunstan, founder"></div>
  </div>

  <div class="person">
    <h1 class="person__name">MIRELA DUNSTAN</h1>
    <p class="person__role">Founder</p>
    <p class="person__specialism">Postgraduate Autism (Children) Specialist (with Merit)</p>
    <p class="person__qualification">Qualified by the Faculty of Learning Support and Access Studies<br>(FLSA), Harwell Vale University</p>
  </div>

  <div class="contacts back__contacts">
    <span class="contact">
      <svg viewBox="0 0 14 14" aria-hidden="true"><circle cx="7" cy="7" r="7" fill="var(--yellow)"/><path d="M4.3,3.6 l1.4,-0.4 0.7,1.8 -0.8,0.6 q0.6,1.5 2,2.3 l0.7,-0.7 1.7,0.8 -0.4,1.4 q-3.8,0.2 -5.3,-5.8z" fill="var(--navy)"/></svg>
      +64 937 615 48
    </span>
    <span class="contact">
      <svg viewBox="0 0 14 14" aria-hidden="true"><circle cx="7" cy="7" r="7" fill="var(--yellow)"/><path d="M4.3,3.6 l1.4,-0.4 0.7,1.8 -0.8,0.6 q0.6,1.5 2,2.3 l0.7,-0.7 1.7,0.8 -0.4,1.4 q-3.8,0.2 -5.3,-5.8z" fill="var(--navy)"/></svg>
      +64 20 6283 9150
    </span>
    <span class="contact">
      <svg viewBox="0 0 14 14" aria-hidden="true"><circle cx="7" cy="7" r="7" fill="var(--yellow)"/><rect x="3.5" y="4.5" width="7" height="5" rx="0.6" fill="var(--navy)"/><path d="M3.8,4.9 L7,7.3 10.2,4.9" stroke="var(--yellow)" stroke-width="0.8" fill="none"/></svg>
      mirela@brightpathlearn.nz
    </span>
  </div>
</section>

</body>
</html>
```